Valmora Holdings - Tidal Crest Car Wash automatic car wash signage

We are wanting to have a new automatic car wash sign designed. Our current one is dated and there are numerous options that are no longer available. We like the look of a clean sharp design in keeping with the Tidal Crest colours; orange and blues. The sign should have the Ultimate and Premium options, the "Tidal Crest" and Tidal Crest Car Wash designed in a clean, concise and cool manner.

Font styles to use
Sans Serif

Colors
f37122
3276b5
0255a3
34a7d8

Requirements
Must have
• This project must have the Ultimate and Premium options, the "bucket" and the Tidal Crest Car Wash title. The orange is a key colour with blues for water.

```html
<!DOCTYPE html>
<html lang="en">
<head>
<meta charset="utf-8">
<title>Tidal Crest Car Wash – Wash Menu Sign</title>
<link rel="stylesheet" href="https://fonts.googleapis.com/css2?family=Lilita+One&family=Orbitron:wght@700;900&family=Russo+One&display=swap">
<style>
  :root {
    --orange: #f37122;
    --blue-mid: #3276b5;
    --blue-deep: #0255a3;
    --blue-sky: #34a7d8;
    --row-panel: #2a64b3;
    --white: #ffffff;
    --stage: #e6eaee;
    --water-light: #d9effb;
    --water-mid: #7cc6ee;
  }
  * { margin: 0; padding: 0; box-sizing: border-box; }
  html, body {
    width: 1200px; height: 801px; overflow: hidden;
    background: var(--stage);
  }
  .sign {
    position: absolute; left: 0; top: 118px;
    width: 1200px; height: 565px; overflow: hidden;
    background: var(--white);
  }
  .water-backdrop {
    position: absolute; inset: 0;
    background:
      linear-gradient(172deg, var(--blue-sky) 0%, var(--water-light) 22%, var(--white) 40%, var(--white) 55%, var(--water-light) 68%, var(--water-mid) 86%, var(--blue-sky) 100%);
  }
  .badge {
    position: absolute; left: 30px; top: -9px;
    width: 262px; height: 262px; border-radius: 50%;
    background: var(--white);
    border: 18px solid var(--blue-mid);
    box-shadow: inset 0 0 0 4px var(--blue-deep);
    display: flex; align-items: center; justify-content: center;
  }
  .badge-name {
    font-family: "Russo One", sans-serif;
    font-size: 34px; line-height: 1.05; text-align: center;
    color: var(--orange);
  }
  .title-bar {
    position: absolute; left: 273px; top: 36px;
    width: 869px; height: 128px;
    background: var(--blue-deep);
    border-radius: 0 64px 64px 0;
    border-bottom: 7px solid var(--orange);
    display: flex; align-items: center; justify-content: center;
  }
  .title {
    font-family: "Lilita One", sans-serif;
    font-size: 62px; letter-spacing: 1px;
    color: var(--orange); text-transform: uppercase;
    white-space: nowrap;
  }
  .plan-head {
    position: absolute; top: 178px; height: 44px; width: 176px;
    border-radius: 16px 16px 4px 4px;
    color: var(--white); text-align: center;
    font-family: "Orbitron", sans-serif; font-weight: 900;
  }
  .plan-head.ultimate { left: 734px; background: var(--orange); }
  .plan-head.premium { left: 911px; background: var(--blue-deep); }
  .plan-name { display: block; font-size: 13px; line-height: 1; padding-top: 3px; letter-spacing: 0.5px; }
  .plan-price { display: block; font-size: 24px; line-height: 1.05; }
  .features {
    position: absolute; left: 287px; top: 222px;
    width: 452px; height: 310px;
    background: var(--row-panel);
    border-radius: 12px 0 0 12px;
    list-style: none;
  }
  .features li {
    height: 31px; line-height: 31px;
    padding-left: 18px;
    font-family: "Russo One", sans-serif; font-size: 17.5px; letter-spacing: 1.2px;
    color: var(--white);
    border-bottom: 1px solid rgba(255,255,255,0.75);
  }
  .features li:last-child { border-bottom: none; }
  .plan-col {
    position: absolute; top: 222px; height: 310px; width: 178px;
    border-radius: 0 0 14px 14px;
  }
  .plan-col.ultimate { left: 739px; background: var(--blue-sky); }
  .plan-col.premium { left: 920px; background: var(--orange); border-radius: 14px; }
  .plan-col svg { display: block; }
</style>
</head>
<body>
  <main class="sign">
    <div class="water-backdrop" role="img" aria-label="Soft blue water waves with splashing droplets across the sign background"></div>

    <div class="badge"><span class="badge-name">Tidal<br>Crest</span></div>

    <header class="title-bar">
      <h1 class="title">Tidal Crest Car Wash</h1>
    </header>

    <div class="plan-head ultimate"><span class="plan-name">ULTIMATE</span><span class="plan-price">$1400</span></div>
    <div class="plan-head premium"><span class="plan-name">PREMIUM</span><span class="plan-price">$1200</span></div>

    <ul class="features">
      <li>Windshield &amp; Front Bug Wash</li>
      <li>Under Carriage &amp; Wheel Blaster</li>
      <li>Extra Pass of High Pressure Wash</li>
      <li>Tri Foam Conditioner / Cleaner</li>
      <li>Side Kick Dryers</li>
      <li>Wax / Surface Protectant</li>
      <li>On Board Overhead Dryer</li>
      <li>Two Passes of Pre-Soak</li>
      <li>High Pressure Wash Pass</li>
      <li>Spot Free Rinse</li>
    </ul>

    <div class="plan-col ultimate">
      <svg width="178" height="310" viewBox="0 0 178 310" aria-label="Ultimate includes all ten services">
        <g fill="none" stroke="#ffffff" stroke-width="4" stroke-linecap="round" stroke-linejoin="round">
          <line x1="0" y1="31" x2="178" y2="31" stroke-width="1" stroke-opacity="0.7"/>
          <line x1="0" y1="62" x2="178" y2="62" stroke-width="1" stroke-opacity="0.7"/>
          <line x1="0" y1="93" x2="178" y2="93" stroke-width="1" stroke-opacity="0.7"/>
          <line x1="0" y1="124" x2="178" y2="124" stroke-width="1" stroke-opacity="0.7"/>
          <line x1="0" y1="155" x2="178" y2="155" stroke-width="1" stroke-opacity="0.7"/>
          <line x1="0" y1="186" x2="178" y2="186" stroke-width="1" stroke-opacity="0.7"/>
          <line x1="0" y1="217" x2="178" y2="217" stroke-width="1" stroke-opacity="0.7"/>
          <line x1="0" y1="248" x2="178" y2="248" stroke-width="1" stroke-opacity="0.7"/>
          <line x1="0" y1="279" x2="178" y2="279" stroke-width="1" stroke-opacity="0.7"/>
          <polyline points="78,9 87,20 101,5"/>
          <polyline points="78,40 87,51 101,36"/>
          <polyline points="78,71 87,82 101,67"/>
          <polyline points="78,102 87,113 101,98"/>
          <polyline points="78,133 87,144 101,129"/>
          <polyline points="78,164 87,175 101,160"/>
          <polyline points="78,195 87,206 101,191"/>
          <polyline points="78,226 87,237 101,222"/>
          <polyline points="78,257 87,268 101,253"/>
          <polyline points="78,288 87,299 101,284"/>
        </g>
      </svg>
    </div>

    <div class="plan-col premium">
      <svg width="178" height="310" viewBox="0 0 178 310" aria-label="Premium includes six of the services">
        <g fill="none" stroke="#ffffff" stroke-width="4" stroke-linecap="round" stroke-linejoin="round">
          <line x1="0" y1="31" x2="178" y2="31" stroke-width="1" stroke-opacity="0.7"/>
          <line x1="0" y1="62" x2="178" y2="62" stroke-width="1" stroke-opacity="0.7"/>
          <line x1="0" y1="93" x2="178" y2="93" stroke-width="1" stroke-opacity="0.7"/>
          <line x1="0" y1="124" x2="178" y2="124" stroke-width="1" stroke-opacity="0.7"/>
          <line x1="0" y1="155" x2="178" y2="155" stroke-width="1" stroke-opacity="0.7"/>
          <line x1="0" y1="186" x2="178" y2="186" stroke-width="1" stroke-opacity="0.7"/>
          <line x1="0" y1="217" x2="178" y2="217" stroke-width="1" stroke-opacity="0.7"/>
          <line x1="0" y1="248" x2="178" y2="248" stroke-width="1" stroke-opacity="0.7"/>
          <line x1="0" y1="279" x2="178" y2="279" stroke-width="1" stroke-opacity="0.7"/>
          <polyline points="78,40 87,51 101,36"/>
          <polyline points="78,133 87,144 101,129"/>
          <polyline points="78,195 87,206 101,191"/>
          <polyline points="78,226 87,237 101,222"/>
          <polyline points="78,257 87,268 101,253"/>
          <polyline points="78,288 87,299 101,284"/>
        </g>
      </svg>
    </div>
  </main>
</body>
</html>
```